Postcard Design Project A Healthy reminder

Dr.'s Deepesh and Nadia sethi. Internal Medicine/Family practice. This postcard will be for our patients that we have not seen in a while. Also we need another postcard (the one your designing) with a different heading for New patient's. Do you offer a price break for that? The only thing we would need to change is the heading. Please let me know. Thank you so much! Also can you use the map on the last postcard and our logo I made? I cant find it. Please feel free to call me or email me.

```html
<!DOCTYPE html>
<html lang="en">
<head>
<meta charset="utf-8">
<title>Sethi M.D. – Friendly Reminder Postcard</title>
<link href="https://fonts.googleapis.com/css2?family=PT+Sans:wght@400;700&family=PT+Sans+Narrow:wght@400;700&display=swap" rel="stylesheet">
<style>
  :root {
    --backdrop: #e9e6e1;
    --red: #9e1b1e;
    --red-deep: #7a1315;
    --black: #1b1a1a;
    --white: #ffffff;
    --ink: #231f20;
    --grey: #6d6e71;
    --photo-a: #c9c3bd;
    --photo-b: #8a7f78;
  }
  * { box-sizing: border-box; margin: 0; padding: 0; }
  html, body { width: 1200px; height: 489px; overflow: hidden; }
  body { background: var(--backdrop); position: relative; font-family: "PT Sans", Arial, sans-serif; }

  .postcard {
    position: absolute; top: 47px; width: 553px; height: 381px;
    background: var(--white); overflow: hidden;
    box-shadow: 0 2px 6px rgba(0,0,0,.25);
  }
  .postcard--front { left: 35px; }
  .postcard--back { left: 612px; }
  .postcard svg.shapes { position: absolute; inset: 0; }
  .abs { position: absolute; }

  /* front */
  .reminder-kicker { left: 30px; top: 16px; color: var(--white); font-size: 22px; letter-spacing: .3px; }
  .reminder-title { left: 30px; top: 42px; color: var(--white); font-size: 23.5px; font-weight: 700; line-height: 30px; }
  .brand-name { left: 70px; top: 224px; color: var(--ink); font-size: 19px; font-weight: 700; }
  .brand-tag { left: 100px; top: 298px; color: var(--ink); font-size: 10px; font-weight: 700; letter-spacing: .6px; }
  .front-contact { left: 370px; top: 290px; width: 175px; color: var(--white); text-align: center; font-family: "PT Sans Narrow", Arial, sans-serif; font-size: 14px; line-height: 17px; }
  .front-contact .phone { margin-top: 10px; font-family: "PT Sans", Arial, sans-serif; font-weight: 700; font-size: 14px; }
  .front-contact .web { margin-top: 3px; font-family: "PT Sans", Arial, sans-serif; font-size: 13.5px; }
  .phone svg { width: 12px; height: 12px; vertical-align: -1px; margin-right: 2px; }

  /* back */
  .about-title { left: 25px; top: 19px; font-size: 16px; font-weight: 700; color: var(--ink); }
  .about-body { left: 25px; top: 44px; width: 238px; font-family: "PT Sans Narrow", Arial, sans-serif; font-size: 12.4px; line-height: 16px; color: var(--ink); }
  .about-body b { font-weight: 700; }
  .about-cta { left: 25px; top: 264px; width: 232px; text-align: center; font-family: "PT Sans Narrow", Arial, sans-serif; font-weight: 700; font-size: 13.5px; color: var(--ink); line-height: 18px; }
  .about-cta .phone { color: var(--red); font-family: "PT Sans", Arial, sans-serif; font-size: 14px; margin-top: 3px; }
  .about-cta .web { font-family: "PT Sans", Arial, sans-serif; font-size: 14px; }
  .mail-name { left: 345px; top: 40px; font-size: 9px; font-weight: 700; color: var(--ink); }
  .mail-address { left: 343px; top: 79px; font-family: "PT Sans Narrow", Arial, sans-serif; font-size: 12px; line-height: 16px; color: var(--ink); }
  .stamp-box { left: 475px; top: 20px; width: 58px; height: 70px; border: 2.5px solid var(--grey); }
</style>
</head>
<body>

<section class="postcard postcard--front">
  <svg class="shapes" viewBox="0 0 553 381" width="553" height="381">
    <defs>
      <linearGradient id="photoTone" x1="0" y1="0" x2="1" y2="1">
        <stop offset="0" stop-color="var(--photo-a)"/>
        <stop offset="1" stop-color="var(--photo-b)"/>
      </linearGradient>
    </defs>
    <path d="M0 0 H553 V48 C460 60 360 110 250 140 C160 164 70 168 0 160 Z" fill="var(--red)"/>
    <path d="M0 160 C70 168 160 164 250 140 C330 118 380 100 430 86 C360 118 300 150 230 166 C150 184 60 180 0 174 Z" fill="var(--black)"/>
    <path d="M0 330 C120 345 250 325 340 295 C410 275 480 272 553 272 V381 H0 Z" fill="var(--black)"/>
    <path d="M0 330 C120 345 250 325 340 295 C300 322 220 344 120 350 C70 352 30 346 0 342 Z" fill="var(--red)"/>
    <path d="M345 78 C318 150 318 225 342 288" fill="none" stroke="var(--red)" stroke-width="6"/>
    <path role="img" aria-label="Photo of two doctors reviewing a patient chart in a clinic hallway" d="M352 72 C392 62 470 56 553 54 V272 C480 272 410 276 352 290 C330 225 330 140 352 72 Z" fill="url(#photoTone)"/>
  </svg>

  <p class="abs reminder-kicker">JUST A FRIENDLY REMINDER</p>
  <h1 class="abs reminder-title">Our records show that it is<br>time for your next visit</h1>

  <p class="abs brand-name">Deepesh T Sethi, M.D.</p>
  <p class="abs brand-tag">A Primary Care Office</p>

  <div class="abs front-contact">
    <p>4820 N. Cedar Ave Suite 210<br>Fresno, Ca 93726</p>
    <p class="phone"><svg viewBox="0 0 12 12"><circle cx="6" cy="6" r="5.3" fill="none" stroke="currentColor" stroke-width="1"/><path d="M4 3 L5 3 L5.6 4.6 L4.9 5.2 C5.3 6 5.9 6.7 6.8 7.1 L7.4 6.4 L9 7 L9 8 C6.5 8.5 3.5 5.5 4 3 Z" fill="currentColor"/></svg>559.555.0142</p>
    <p class="web">SethiMD.com</p>
  </div>
</section>

<section class="postcard postcard--back">
  <svg class="shapes" viewBox="0 0 553 381" width="553" height="381">
    <defs>
      <linearGradient id="swoosh" x1="0" y1="0" x2="1" y2="0">
        <stop offset="0" stop-color="var(--red)" stop-opacity="0.15"/>
        <stop offset="1" stop-color="var(--red)"/>
      </linearGradient>
    </defs>
    <path d="M200 0 H232 C300 90 315 230 265 381 H250 C290 240 280 100 200 0 Z" fill="url(#swoosh)"/>
    <path d="M262 40 C300 120 305 240 275 330 C292 240 290 130 262 40 Z" fill="var(--red-deep)"/>
  </svg>

  <h2 class="abs about-title">About Our Practice</h2>
  <p class="abs about-body">Our Primary Care/ Internal Medicine practice provides an array of comprehensive medical services. Our practice is committed to providing coordinated and continuous healthcare. Primary Care Physician Dr. Nadia Sethi aims to provide patients with a broad spectrum of preventative and curative care. Primary healthcare treats the whole human body, rather than specific organs or systems. Internal Medicine Physician <b>Dr. Deepesh T. Sethi</b> specializes with the prevention, diagnosis, and treatment of adult diseases, and is especially skilled in the management of patients who have undifferentiated or multi-system diseases.</p>

  <div class="abs about-cta">
    <p>Call today to schedule an appointment</p>
    <p class="phone"><svg viewBox="0 0 12 12"><circle cx="6" cy="6" r="5.3" fill="none" stroke="currentColor" stroke-width="1"/><path d="M4 3 L5 3 L5.6 4.6 L4.9 5.2 C5.3 6 5.9 6.7 6.8 7.1 L7.4 6.4 L9 7 L9 8 C6.5 8.5 3.5 5.5 4 3 Z" fill="currentColor"/></svg>559.555.0142</p>
    <p class="web">SethiMD.com</p>
  </div>

  <p class="abs mail-name">Deepesh T Sethi, M.D.</p>
  <p class="abs mail-address">4820 N. Cedar Ave Suite 210<br>Fresno, Ca 93726</p>
  <div class="abs stamp-box"></div>
</section>

</body>
</html>
```